PPT Template for an investment fund to use in their pitchbooks

Our firm is an international investment fund and are seeking a PPT template to use in our pitch book (and subsequent PPTs). We would need a template for a title slide and then subsequent text/info slides. A clean & uncluttered feel is preferred as well as no watermark on slides. Please see our logo attached. The logo color code is #19478d. Font is Gotham-Medium.

Target Market(s)

Sophisticated investors

Industry/Entity Type

Finance

Colors
ffffff
0356a4

```html
<!DOCTYPE html>
<html lang="en">
<head>
<meta charset="utf-8">
<title>Kestrel Litigation Funding – Presentation Template</title>
<link rel="stylesheet" href="https://fonts.googleapis.com/css2?family=Montserrat:wght@300;400;500;600;700&family=Open+Sans:wght@400;600&display=swap">
<style>
:root{
  --blue:#19478d;
  --blue-bright:#0356a4;
  --backdrop:#4a4a4a;
  --white:#ffffff;
  --grey-light:#e6e7e8;
  --grey-mid:#c9cacc;
  --grey-dark:#3c3d3f;
  --text-dark:#2b2b2b;
}
*{margin:0;padding:0;box-sizing:border-box}
html,body{width:1200px;height:1014px;overflow:hidden}
body{
  background:radial-gradient(ellipse at center,#5a5a5a 0%,var(--backdrop) 70%,#3e3e3e 100%);
  position:relative;
  font-family:"Montserrat",sans-serif;
}
.slide{
  position:absolute;width:508px;height:285px;background:var(--white);
  overflow:hidden;box-shadow:0 6px 18px rgba(0,0,0,.45);
}
.slide>svg.frame{position:absolute;left:0;top:0;width:508px;height:285px}
.slide--title{left:50px;top:47px}
.slide--partners{left:636px;top:47px}
.slide--values{left:50px;top:375px}
.slide--gradient{left:636px;top:375px}
.slide--cycle{left:50px;top:692px}
.slide--thanks{left:636px;top:692px}

.photo{position:absolute}
.photo--columns{left:243px;top:0;width:192px;height:40px;
  background:linear-gradient(90deg,rgba(230,231,232,1) 0%,#d7d7d5 25%,#f1f1ef 45%,#c8c8c6 65%,#ecebe9 85%,#dcdcda 100%)}
.slide-title{position:absolute;left:43px;top:14px;font-weight:700;font-size:12.5px;color:var(--blue);letter-spacing:.3px}

.title-top{position:absolute;right:150px;top:18px;font-weight:300;font-size:26px;color:#333;letter-spacing:.5px}
.title-main{position:absolute;right:150px;top:46px;font-weight:700;font-size:33px;color:var(--blue);letter-spacing:.5px}
.brand{position:absolute;color:var(--blue);font-weight:600;text-align:center;line-height:1.1}
.brand--title{left:30px;top:250px;width:140px;font-size:10px}
.brand--title small{display:block;font-size:6px;letter-spacing:3px}
.title-url{position:absolute;left:378px;top:254px;font-family:"Open Sans",sans-serif;font-size:6.5px;color:var(--white)}

.bullets{position:absolute;left:44px;top:87px;list-style:none;font-weight:500;font-size:11.5px;color:#222}
.bullets li{height:23.6px;display:flex;align-items:center}
.bullets li::before{content:"»";color:var(--blue);font-weight:700;font-size:13px;margin-right:6px;line-height:1}

.values{position:absolute;left:41px;top:80px;list-style:none}
.values li{position:relative;width:244px;height:21px;margin-bottom:20px;border-radius:11px;background:#ececec;
  font-family:"Open Sans",sans-serif;font-size:8.5px;color:#222;display:flex;align-items:center;padding-left:53px}
.values li svg{position:absolute;left:11px;top:-6px;width:33px;height:33px}
</style>
</head>
<body>

<svg width="0" height="0" style="position:absolute">
  <defs>
    <linearGradient id="soft-blue" x1="0" y1="1" x2="1" y2="0">
      <stop offset="0" stop-color="#dbe8f8"/><stop offset="1" stop-color="#ffffff"/>
    </linearGradient>
    <g id="content-frame">
      <rect x="0" y="0" width="508" height="40" fill="#e6e7e8"/>
      <polygon points="452,0 508,0 508,8 474,40 418,40" fill="#e9eaeb"/>
      <polygon points="416,0 486,0 445,40 373,40" fill="#19478d"/>
      <polygon points="0,264 5,264 26,285 0,285" fill="#19478d"/>
      <polygon points="9,262 15,262 38,285 32,285" fill="#c9cacc"/>
      <polygon points="26,265 372,265 392,285 46,285" fill="#19478d"/>
      <polygon points="378,265 388,265 408,285 398,285" fill="#3c3d3f"/>
      <polygon points="392,265 398,265 418,285 412,285" fill="#c9cacc"/>
      <polygon points="476,253 508,253 508,285" fill="#a9aaac"/>
      <g font-family="Open Sans, sans-serif" font-size="5.4" fill="#ffffff">
        <text x="236" y="278">Wellington</text>
        <text x="271" y="278" fill="#9fb5d8">|</text>
        <text x="270" y="278" dx="6">Brisbane</text>
        <text x="306" y="278" fill="#9fb5d8">|</text>
        <text x="310" y="278">Canberra</text>
        <text x="341" y="278" fill="#9fb5d8">|</text>
        <text x="345" y="278">London</text>
      </g>
      <g font-family="Montserrat, sans-serif" font-weight="600" fill="#19478d" text-anchor="middle">
        <text x="442" y="270" font-size="5.6">KESTREL LITIGATION</text>
        <text x="442" y="276" font-size="3.4" letter-spacing="1.4">FUNDING</text>
      </g>
    </g>
  </defs>
</svg>

<!-- Title slide -->
<section class="slide slide--title">
  <svg class="frame" viewBox="0 0 508 285">
    <rect x="0" y="100" width="200" height="185" fill="url(#soft-blue)"/>
    <polygon points="38,0 122,0 362,232 272,232" fill="#e3e4e6"/>
    <polygon points="0,0 38,0 272,232 508,232 508,285 292,285 0,52" fill="#19478d"/>
    <polygon points="0,52 292,285 0,285" fill="#ffffff" opacity="0"/>
    <polygon points="0,58 286,285 250,285 0,92" fill="#ffffff"/>
    <polygon points="0,118 0,140 68,200 82,200" fill="#19478d"/>
    <polygon points="129,155 158,155 288,285 258,285" fill="#19478d"/>
    <line x1="430" y1="268" x2="508" y2="268" stroke="#ffffff" stroke-width=".8"/>
    <circle cx="430" cy="268" r="1.6" fill="#ffffff"/>
  </svg>
  <div class="photo" role="img" aria-label="Photo: hand holding a magnifying glass over banknotes between a red and a green figure" style="left:258px;top:0;width:250px;height:190px;background:radial-gradient(ellipse at 60% 55%,#e4e6e3 0%,#f3f3f2 45%,#ffffff 75%)"></div>
  <div class="title-top">Litigation</div>
  <div class="title-main">FUNDING</div>
  <div class="brand brand--title">KESTREL LITIGATION<small>FUNDING</small></div>
  <div class="title-url">www.KestrelLitigationFunding.com</div>
</section>

<!-- Partners slide -->
<section class="slide slide--partners">
  <svg class="frame" viewBox="0 0 508 285">
    <polygon points="508,200 508,265 360,265" fill="#f4f4f5"/>
    <use href="#content-frame"/>
    <g fill="#d3d6db">
      <rect x="382" y="82" width="58" height="12" rx="2"/>
      <rect x="382" y="109" width="58" height="14" rx="2"/>
      <rect x="382" y="139" width="58" height="14" rx="2"/>
      <rect x="382" y="171" width="58" height="20" rx="2"/>
      <rect x="382" y="205" width="62" height="13" rx="2"/>
    </g>
  </svg>
  <div class="photo photo--columns" role="img" aria-label="Photo: classical stone columns"></div>
  <h2 class="slide-title">LOREM IPSUM DOLOR</h2>
  <ul class="bullets">
    <li>Lorem ipsum dolor sit amet</li>
    <li>consectetur adipiscing elit, sed do</li>
    <li>eiusmod tempor incididunt ut</li>
    <li>labore et dolore magna aliqua</li>
    <li>Ut enim ad minim veniam</li>
    <li>quis nostrud exercitation ullamco</li>
  </ul>
</section>

<!-- Values slide -->
<section class="slide slide--values">
  <svg class="frame" viewBox="0 0 508 285"><use href="#content-frame"/></svg>
  <div class="photo photo--columns" role="img" aria-label="Photo: classical stone columns"></div>
  <div class="photo" role="img" aria-label="Photo: wooden judge's gavel on a sound block" style="left:328px;top:18px;width:180px;height:220px;clip-path:polygon(100% 0,100% 100%,0 100%);background:linear-gradient(135deg,#6f8f4a 0%,#a9b98a 40%,#9a6a3d 70%,#6b4424 100%)"></div>
  <h2 class="slide-title">LOREM IPSUM DOLOR</h2>
  <ul class="values">
    <li><svg viewBox="0 0 33 33"><circle cx="16.5" cy="16.5" r="15.5" fill="#19478d" stroke="#fff" stroke-width="1.5"/><g fill="none" stroke="#fff" stroke-width="1"><circle cx="12" cy="11" r="2"/><circle cx="16.5" cy="10" r="2"/><circle cx="21" cy="11" r="2"/><path d="M9 20h15M10 23l4-3h8"/></g></svg>Deliver value for staff and customers</li>
    <li><svg viewBox="0 0 33 33"><circle cx="16.5" cy="16.5" r="15.5" fill="#19478d" stroke="#fff" stroke-width="1.5"/><g fill="none" stroke="#fff" stroke-width="1"><circle cx="16.5" cy="15" r="5"/><circle cx="16.5" cy="15" r="2"/><path d="M14.5 21h4M15 23h3"/></g></svg>Innovate adapt and improve</li>
    <li><svg viewBox="0 0 33 33"><circle cx="16.5" cy="16.5" r="15.5" fill="#19478d" stroke="#fff" stroke-width="1.5"/><g fill="none" stroke="#fff" stroke-width="1"><rect x="8" y="11" width="11" height="8" rx="3"/><rect x="14" y="14" width="11" height="8" rx="3"/></g></svg>Walk the talk, recommend and implement</li>
    <li><svg viewBox="0 0 33 33"><circle cx="16.5" cy="16.5" r="15.5" fill="#19478d" stroke="#fff" stroke-width="1.5"/><g fill="none" stroke="#fff" stroke-width="1"><circle cx="14" cy="12" r="3"/><path d="M9 23c0-4 2-6 5-6s5 2 5 6M19 14l4 4-4 4"/></g></svg>Be honest and transparent</li>
  </ul>
</section>

<!-- Gradient infographic slide -->
<section class="slide slide--gradient">
  <svg class="frame" viewBox="0 0 508 285">
    <use href="#content-frame"/>
    <defs>
      <linearGradient id="g1" x1="0" x2="1"><stop offset="0" stop-color="#f7a81b"/><stop offset="1" stop-color="#f2542d"/></linearGradient>
      <linearGradient id="g2" x1="0" x2="1"><stop offset="0" stop-color="#33b6e6"/><stop offset="1" stop-color="#8a5cf0"/></linearGradient>
      <linearGradient id="g3" x1="0" x2="1"><stop offset="0" stop-color="#f2473a"/><stop offset="1" stop-color="#ef3d6e"/></linearGradient>
      <linearGradient id="g4" x1="0" x2="1"><stop offset="0" stop-color="#6bc84a"/><stop offset="1" stop-color="#14a89a"/></linearGradient>
      <linearGradient id="g5" x1="0" x2="1"><stop offset="0" stop-color="#e23b6b"/><stop offset="1" stop-color="#7b3fa0"/></linearGradient>
    </defs>
    <circle cx="88" cy="157" r="47" fill="#b9bcc0"/>
    <circle cx="88" cy="157" r="42" fill="#ffffff"/>
    <text x="88" y="147" text-anchor="middle" font-family="Montserrat, sans-serif" font-weight="700" font-size="11.5" fill="#333">Gradient</text>
    <text x="88" y="154" text-anchor="middle" font-family="Montserrat, sans-serif" font-size="4.2" letter-spacing="1.2" fill="#888">INFOGRAPHIC</text>
    <ellipse cx="88" cy="167" rx="18" ry="7" fill="#d4d6d9"/>
    <path d="M118 110 Q125 95 146 72" fill="none" stroke="#f7a81b" stroke-width=".9" stroke-dasharray="1.5 2"/>
    <path d="M135 128 Q140 112 150 112" fill="none" stroke="#33b6e6" stroke-width=".9" stroke-dasharray="1.5 2"/>
    <path d="M143 157 L152 152" fill="none" stroke="#f2473a" stroke-width=".9" stroke-dasharray="1.5 2"/>
    <path d="M137 184 Q142 192 152 192" fill="none" stroke="#6bc84a" stroke-width=".9" stroke-dasharray="1.5 2"/>
    <path d="M115 205 Q125 225 152 232" fill="none" stroke="#e23b6b" stroke-width=".9" stroke-dasharray="1.5 2"/>
    <g fill="#fff" stroke-width="1.3">
      <circle cx="116" cy="108" r="2.2" stroke="#f7a81b"/><circle cx="135" cy="126" r="2.2" stroke="#33b6e6"/>
      <circle cx="143" cy="157" r="2.2" stroke="#f2473a"/><circle cx="137" cy="186" r="2.2" stroke="#6bc84a"/>
      <circle cx="115" cy="207" r="2.2" stroke="#e23b6b"/>
    </g>
    <g font-family="Montserrat, sans-serif">
      <g>
        <rect x="168" y="60" width="94" height="22" rx="11" fill="url(#g1)"/>
        <circle cx="182" cy="71" r="15" fill="url(#g1)"/><circle cx="182" cy="71" r="12" fill="#fff"/><circle cx="182" cy="71" r="7" fill="#f7a81b"/>
        <text x="202" y="67" font-size="3.6" font-weight="700" fill="#fff">TITLE GOES HERE</text>
        <text x="202" y="73" font-size="2.5" fill="#fff">Short note goes here</text>
      </g>
      <g>
        <rect x="168" y="101" width="94" height="22" rx="11" fill="url(#g2)"/>
        <circle cx="182" cy="112" r="15" fill="url(#g2)"/><circle cx="182" cy="112" r="12" fill="#fff"/><circle cx="182" cy="112" r="7" fill="#33b6e6"/>
        <text x="202" y="108" font-size="3.6" font-weight="700" fill="#fff">TITLE GOES HERE</text>
        <text x="202" y="114" font-size="2.5" fill="#fff">Short note goes here</text>
      </g>
      <g>
        <rect x="168" y="141" width="94" height="22" rx="11" fill="url(#g3)"/>
        <circle cx="182" cy="152" r="15" fill="url(#g3)"/><circle cx="182" cy="152" r="12" fill="#fff"/><circle cx="182" cy="152" r="7" fill="#f2473a"/>
        <text x="202" y="148" font-size="3.6" font-weight="700" fill="#fff">TITLE GOES HERE</text>
        <text x="202" y="154" font-size="2.5" fill="#fff">Short note goes here</text>
      </g>
      <g>
        <rect x="168" y="181" width="94" height="22" rx="11" fill="url(#g4)"/>
        <circle cx="182" cy="192" r="15" fill="url(#g4)"/><circle cx="182" cy="192" r="12" fill="#fff"/><circle cx="182" cy="192" r="7" fill="#3bb86f"/>
        <text x="202" y="188" font-size="3.6" font-weight="700" fill="#fff">TITLE GOES HERE</text>
        <text x="202" y="194" font-size="2.5" fill="#fff">Short note goes here</text>
      </g>
      <g>
        <rect x="168" y="221" width="94" height="22" rx="11" fill="url(#g5)"/>
        <circle cx="182" cy="232" r="15" fill="url(#g5)"/><circle cx="182" cy="232" r="12" fill="#fff"/><circle cx="182" cy="232" r="7" fill="#c13c7e"/>
        <text x="202" y="228" font-size="3.6" font-weight="700" fill="#fff">TITLE GOES HERE</text>
        <text x="202" y="234" font-size="2.5" fill="#fff">Short note goes here</text>
      </g>
    </g>
  </svg>
  <div class="photo photo--columns" role="img" aria-label="Photo: classical stone columns"></div>
  <div class="photo" role="img" aria-label="Photo: money sack and wooden figure on a balance scale under a magnifying glass" style="left:286px;top:18px;width:222px;height:220px;clip-path:polygon(100% 0,100% 100%,0 100%);background:linear-gradient(135deg,#a88a63 0%,#7d7c7a 45%,#4f5052 75%,#c9a979 100%)"></div>
  <h2 class="slide-title">LOREM IPSUM DOLOR</h2>
</section>

<!-- Cycle infographic slide -->
<section class="slide slide--cycle">
  <svg class="frame" viewBox="0 0 508 285">
    <use href="#content-frame"/>
    <g stroke="#555" stroke-width=".6" stroke-dasharray="1 1.5">
      <line x1="167" y1="101" x2="167" y2="120"/><line x1="167" y1="192" x2="167" y2="205"/>
      <line x1="127" y1="156" x2="115" y2="156"/><line x1="207" y1="156" x2="220" y2="156"/>
      <line x1="139" y1="128" x2="130" y2="119"/><line x1="195" y1="128" x2="205" y2="119"/>
      <line x1="139" y1="184" x2="130" y2="192"/><line x1="195" y1="184" x2="205" y2="192"/>
    </g>
    <circle cx="167" cy="156" r="36" fill="#f1f1f2" stroke="#fff" stroke-width="3"/>
    <text x="167" y="155" text-anchor="middle" font-family="Montserrat, sans-serif" font-weight="600" font-size="8.5" fill="#333">MINIMALIST</text>
    <text x="167" y="162" text-anchor="middle" font-family="Montserrat, sans-serif" font-size="5.5" letter-spacing=".8" fill="#777">INFOGRAPHIC</text>
    <g>
      <circle cx="147" cy="168" r="1.5" fill="#11aab6"/><circle cx="153" cy="168" r="1.5" fill="#1e9bc3"/><circle cx="159" cy="168" r="1.5" fill="#1b7fc4"/><circle cx="165" cy="168" r="1.5" fill="#1c66b8"/><circle cx="171" cy="168" r="1.5" fill="#6a3fb5"/><circle cx="177" cy="168" r="1.5" fill="#a43fb0"/><circle cx="183" cy="168" r="1.5" fill="#cc3d8f"/><circle cx="189" cy="168" r="1.5" fill="#e0527a"/>
    </g>
    <g font-family="Montserrat, sans-serif" text-anchor="middle" fill="#fff">
      <g transform="translate(167 75)"><circle r="28" fill="#fff"/><circle r="25" fill="#11aab6"/><text y="-3" font-size="14" font-weight="600">01</text><text y="3" font-size="2.6">LOREM IPSUM</text><text y="8" font-size="2.2">Short line of note</text><text y="11.5" font-size="2.2">text to fill here</text></g>
      <g transform="translate(223 100)"><circle r="28" fill="#fff"/><circle r="25" fill="#1e9bc3"/><text y="-3" font-size="14" font-weight="600">02</text><text y="3" font-size="2.6">LOREM IPSUM</text><text y="8" font-size="2.2">Short line of note</text><text y="11.5" font-size="2.2">text to fill here</text></g>
      <g transform="translate(246 153)"><circle r="28" fill="#fff"/><circle r="25" fill="#1b7fc4"/><text y="-3" font-size="14" font-weight="600">03</text><text y="3" font-size="2.6">LOREM IPSUM</text><text y="8" font-size="2.2">Short line of note</text></g>
      <g transform="translate(223 208)"><circle r="28" fill="#fff"/><circle r="25" fill="#1c66b8"/><text y="-3" font-size="14" font-weight="600">04</text><text y="3" font-size="2.6">LOREM IPSUM</text><text y="8" font-size="2.2">Short line of note</text></g>
      <g transform="translate(167 231)"><circle r="28" fill="#fff"/><circle r="25" fill="#6a3fb5"/><text y="-3" font-size="14" font-weight="600">05</text><text y="3" font-size="2.6">LOREM IPSUM</text><text y="8" font-size="2.2">Short line of note</text></g>
      <g transform="translate(112 208)"><circle r="28" fill="#fff"/><circle r="25" fill="#a43fb0"/><text y="-3" font-size="14" font-weight="600">06</text><text y="3" font-size="2.6">LOREM IPSUM</text><text y="8" font-size="2.2">Short line of note</text></g>
      <g transform="translate(89 153)"><circle r="28" fill="#fff"/><circle r="25" fill="#cc3d8f"/><text y="-3" font-size="14" font-weight="600">07</text><text y="3" font-size="2.6">LOREM IPSUM</text><text y="8" font-size="2.2">Short line of note</text></g>
      <g transform="translate(112 100)"><circle r="28" fill="#fff"/><circle r="25" fill="#e0527a"/><text y="-3" font-size="14" font-weight="600">08</text><text y="3" font-size="2.6">LOREM IPSUM</text><text y="8" font-size="2.2">Short line of note</text></g>
    </g>
  </svg>
  <div class="photo photo--columns" role="img" aria-label="Photo: classical stone columns"></div>
  <div class="photo" role="img" aria-label="Photo: piggy bank and gavel on a printed financial chart" style="left:290px;top:18px;width:218px;height:220px;clip-path:polygon(100% 0,100% 100%,0 100%);background:linear-gradient(135deg,#dfe3ec 0%,#c9b8c4 40%,#4a4656 62%,#d8c4a8 80%,#a9c58c 100%)"></div>
  <h2 class="slide-title">LOREM IPSUM DOLOR</h2>
</section>

<!-- Closing slide -->
<section class="slide slide--thanks">
  <svg class="frame" viewBox="0 0 508 285">
    <rect x="0" y="0" width="508" height="148" fill="#19478d"/>
    <rect x="0" y="202" width="300" height="29" fill="#19478d"/>
    <polygon points="508,25 304,231 508,231" fill="#ffffff"/>
    <polygon points="470,0 508,0 508,25 304,231 238,231" fill="#3c3d3f"/>
    <polygon points="445,156 462,156 325,285 307,285" fill="#e3e4e6"/>
    <polygon points="508,185 508,231 459,231" fill="#19478d"/>
    <line x1="135" y1="158" x2="135" y2="195" stroke="#333" stroke-width=".7"/>
    <line x1="0" y1="269" x2="78" y2="269" stroke="#19478d" stroke-width=".8"/>
    <circle cx="78" cy="269" r="1.6" fill="#19478d"/>
    <text x="38" y="62" font-family="Montserrat, sans-serif" font-weight="300" font-size="33" letter-spacing="1.5" fill="#ffffff">THANK YOU</text>
    <g font-family="Montserrat, sans-serif" font-weight="600" fill="#19478d" text-anchor="middle">
      <text x="79" y="185" font-size="6.6">KESTREL LITIGATION</text>
      <text x="79" y="191.5" font-size="4" letter-spacing="1.6">FUNDING</text>
    </g>
    <text x="151" y="178" font-family="Open Sans, sans-serif" font-size="6.5" fill="#19478d">www.<tspan font-weight="600">KestrelLitigationFunding</tspan>.com</text>
    <circle cx="424" cy="257" r="8" fill="#3b5b9a"/>
    <circle cx="446" cy="257" r="8" fill="#3a9fdc"/>
    <circle cx="468" cy="257" r="8" fill="#d6336c"/>
  </svg>
</section>

</body>
</html>
```